House flipping business web site needed

birchstoneholdings.example.
I am a residential developer in Northern NJ and I am looking for a fresh new updated website. I have an intro video about my company being made now. I don't update it very often but I want an easy format that I can add update photos to on projects I have worked on or homes I renovate for sale.

Target Market(s)

investors into my projects so a portfolio , people looking to sell their homes to me.

Industry/Entity Type

Real Estate Development

Number of Pages Required

4 page

Font styles to use
Serif

Colors
33b8a4
39a9d7
cadf82

Requirements
Must have
• space for an intro video about my company
• a portfolio with pictures and information about each project
• Markets we serve- Morris County, NJ
• My logo- already created
• SEO
• Yes I would like this to function over all platforms. Phone, computer, all platforms.
• history and background page
• I am looking for a completed page that I can upload to the site that hosts my website
Nice to have
• I want something creative, easy to navigate. modern.

```html
<!DOCTYPE html>
<html lang="en">
<head>
<meta charset="utf-8">
<title>Birchstone Holdings</title>
<link rel="stylesheet" href="https://fonts.googleapis.com/css2?family=Cinzel:wght@400;700&family=Open+Sans:ital,wght@0,400;0,600;0,700;1,400;1,600&display=swap">
<style>
:root{
  --teal:#33b8a4;
  --blue:#39a9d7;
  --band:#3ea2cf;
  --ink:#2b2b2b;
  --muted:#666;
  --dark:#1c1c1c;
  --white:#fff;
  --hero-a:#8d8e8c;
  --hero-b:#4b4a45;
}
*{margin:0;padding:0;box-sizing:border-box}
html,body{width:726px;height:1200px;overflow:hidden;background:var(--white)}
body{position:relative;font-family:"Open Sans",sans-serif;color:var(--ink)}
.abs{position:absolute}
.topline{left:0;top:0;width:726px;height:3px;background:var(--blue)}
.hero{left:0;top:48px;width:726px;height:274px;background:linear-gradient(180deg,var(--hero-a) 0%,#a4a29c 45%,var(--hero-b) 100%)}
.header{left:0;top:3px;width:726px;height:45px;background:var(--white)}
.brand-badge{left:60px;top:0;width:138px;height:116px;background:var(--white);border-radius:0 0 69px 69px;display:flex;align-items:center;justify-content:center;text-align:center;z-index:3}
.brand-badge span{font-family:"Cinzel",serif;font-weight:700;font-size:15px;line-height:18px;color:var(--blue)}
.socials{left:298px;top:7px;display:flex;gap:4px}
.socials i{display:block;width:18px;height:18px;border-radius:50%;background:var(--blue)}
.contact-item{top:8px;display:flex;align-items:center;gap:7px;font-size:10px;color:var(--ink)}
.contact-item .ic{width:18px;height:18px;border:1.5px solid var(--teal);border-radius:50%;display:flex;align-items:center;justify-content:center}
.nav{top:31px;font-size:10px;color:var(--ink)}
.nav.active{color:var(--teal)}
.hero-title{left:0;top:128px;width:726px;text-align:center;font-family:"Cinzel",serif;font-size:38px;color:var(--white);text-shadow:0 2px 4px rgba(0,0,0,.5);letter-spacing:.5px}
.hero-sub{left:0;top:176px;width:726px;text-align:center;font-style:italic;font-weight:600;font-size:14.5px;color:var(--white);text-shadow:0 1px 3px rgba(0,0,0,.6)}
.hero-btn{left:302px;top:207px;width:120px;height:27px;background:var(--teal);color:var(--white);font-size:9.5px;font-weight:700;display:flex;align-items:center;justify-content:center;border-radius:2px}
.dots{left:340px;top:287px;display:flex;gap:2px}
.dots i{width:10px;height:10px;border-radius:50%;border:1px solid var(--white)}
.dots i.on{background:var(--white)}
.welcome h1,.section-title,.foot h3{font-family:"Cinzel",serif;font-weight:400}
.welcome-title{left:60px;top:353px;font-size:15px;color:var(--ink)}
.welcome-text{left:60px;top:381px;width:296px;font-size:7.3px;line-height:14.4px;color:var(--muted)}
.welcome-text p+p{margin-top:11px}
.outline-btn{left:60px;top:506px;width:69px;height:22px;border:1px solid #ccc;border-radius:2px;color:var(--teal);font-size:7.5px;font-weight:700;display:flex;align-items:center;justify-content:center}
.video{left:376px;top:348px;width:290px;height:188px;background:linear-gradient(180deg,#8da866 0%,#6f8f6a 40%,#4a6f88 70%,#5c6e5e 100%)}
.video-bar{left:376px;top:348px;width:290px;height:21px;background:rgba(20,20,20,.9);color:var(--white);font-size:9px;display:flex;align-items:center;justify-content:space-between;padding:0 8px 0 11px}
.play{left:506px;top:427px;width:30px;height:30px;border-radius:50%;background:#111;display:flex;align-items:center;justify-content:center}
.markets{left:0;top:564px;width:726px;height:210px;background:var(--band)}
.section-title{width:726px;left:0;text-align:center}
.markets-title{top:589px;font-size:14px;color:var(--white);letter-spacing:.5px}
.market-img{width:148px;height:114px;border:2px solid var(--white)}
.market-text{width:130px;color:var(--white)}
.market-text h2{font-size:10px;font-weight:600;margin-bottom:8px}
.market-text p{font-size:7.2px;line-height:12.4px}
.market-text a{display:block;margin-top:9px;font-size:7.5px;font-weight:700}
.portfolio-title{top:800px;font-size:15px;color:var(--ink);letter-spacing:.5px}
.proj{width:143px;text-align:center}
.proj .ph{height:106px}
.proj h3{margin-top:10px;font-size:10px;font-weight:600;color:var(--ink)}
.proj p{margin-top:6px;font-size:7.2px;line-height:12.4px;color:var(--muted);padding:0 4px}
.arrow{top:876px}
.foot{left:0;top:1018px;width:726px;height:182px;background:var(--dark);border-top:3px solid var(--blue);color:#ddd}
.foot-brand{left:72px;top:1050px;width:128px;height:84px;display:flex;align-items:center;justify-content:center;text-align:center}
.foot-brand span{font-family:"Cinzel",serif;font-weight:700;font-size:17px;line-height:21px;color:var(--blue)}
.foot h3{font-size:11px;color:var(--white);letter-spacing:.3px}
.foot-links{font-size:7.5px;line-height:17.7px;color:#ddd}
.foot-small{font-size:7.3px;line-height:12px;color:#ddd}
.input{left:354px;top:1090px;width:148px;height:20px;background:var(--white);color:#888;font-size:7px;padding-left:8px;display:flex;align-items:center}
.sub-btn{left:354px;top:1118px;width:60px;height:20px;border:1px solid var(--white);border-radius:2px;color:var(--white);font-size:7.5px;font-weight:700;display:flex;align-items:center;justify-content:center}
.vsep{width:1px;height:96px;background:#333;top:1040px}
.foot-row{left:538px;display:flex;gap:12px;font-size:7.3px;line-height:12.8px;color:#ddd}
.foot-row svg{flex:none;margin-top:2px}
.hsep{left:60px;top:1158px;width:606px;height:1px;background:#333}
.copy{left:60px;top:1173px;font-size:7.3px;color:#ddd}
.foot-social{left:574px;top:1168px;display:flex;gap:4px}
.foot-social i{width:20px;height:20px;border:1.5px solid var(--white);border-radius:50%}
</style>
</head>
<body>
<div class="abs topline"></div>
<div class="abs hero" role="img" aria-label="Photo of a renovated two-storey house with a stone wall and bare trees"></div>
<header class="abs header"></header>
<div class="abs brand-badge"><span>Birchstone<br>Holdings</span></div>
<div class="abs socials"><i></i><i></i><i></i><i></i></div>
<div class="abs contact-item" style="left:392px">
  <span class="ic"><svg width="9" height="9" viewBox="0 0 24 24"><path fill="#33b8a4" d="M6.6 10.8a15 15 0 006.6 6.6l2.2-2.2a1 1 0 011-.25 11.4 11.4 0 003.6.57 1 1 0 011 1V20a1 1 0 01-1 1A17 17 0 013 4a1 1 0 011-1h3.5a1 1 0 011 1 11.4 11.4 0 00.57 3.6 1 1 0 01-.25 1z"/></svg></span>+1 555-014-2290</div>
<div class="abs contact-item" style="left:502px">
  <span class="ic" style="background:var(--teal)"><svg width="9" height="8" viewBox="0 0 24 18"><path fill="#fff" d="M0 0h24v18H0z"/><path fill="none" stroke="#33b8a4" stroke-width="2.5" d="M1 1l11 9 11-9"/></svg></span>info@birchstoneholdings.example</div>
<a class="abs nav active" style="left:442px">Home</a>
<a class="abs nav" style="left:491px">About</a>
<a class="abs nav" style="left:540px">Portfolio</a>
<a class="abs nav" style="left:602px">Contact</a>
<svg class="abs" style="left:657px;top:33px" width="9" height="9" viewBox="0 0 10 10"><circle cx="4" cy="4" r="3" fill="none" stroke="#2b2b2b" stroke-width="1.4"/><path d="M6.2 6.2L9 9" stroke="#2b2b2b" stroke-width="1.6"/></svg>

<div class="abs hero-title">Birchstone Holdings</div>
<div class="abs hero-sub">We are into house flipping business in New Jersey.</div>
<div class="abs hero-btn">GET MORE INFO &gt;&gt;</div>
<div class="abs dots"><i class="on"></i><i></i><i></i><i></i></div>

<section class="welcome">
  <h1 class="abs welcome-title">Welcome to Birchstone Holdings</h1>
  <div class="abs welcome-text">
    <p>We are a team of experienced home buyers and renovators in the Morris County, NJ area. Our specialty is purchasing distressed homes and property.</p>
    <p>We then collaborate with the best talents in Northern New Jersey to renovate those properties and transform them into the best house in the neighborhood. As a result we create equity, a return on investment and most importantly we give home buyers a worry free property that provides a better way of life and hope for their future. We only work in the Morris County area so we are local.</p>
  </div>
  <div class="abs outline-btn">READ MORE &gt;&gt;</div>
  <div class="abs video" role="img" aria-label="Intro video still of a calm lake with a wooded shoreline"></div>
  <div class="abs video-bar"><span>Birchstone Holdings</span>
    <svg width="22" height="10" viewBox="0 0 22 10"><circle cx="5" cy="5" r="4" fill="none" stroke="#fff" stroke-width="1.3"/><path d="M5 3v2.5h1.8" stroke="#fff" stroke-width="1.2" fill="none"/><path d="M13 9c0-4 3-5 6-5V2l3 3-3 3V6c-3 0-5 1-6 3z" fill="#fff"/></svg></div>
  <div class="abs play"><svg width="10" height="11" viewBox="0 0 10 11"><path d="M1 0l9 5.5L1 11z" fill="#fff"/></svg></div>
</section>

<section class="abs markets"></section>
<h2 class="abs section-title markets-title">Markets We Serve</h2>
<div class="abs market-img" style="left:60px;top:633px;background:linear-gradient(160deg,#7fb0d6,#c9a34c 55%,#6e8f3c)" role="img" aria-label="Photo of a stone farmhouse by a pond in autumn"></div>
<div class="abs market-text" style="left:221px;top:630px">
  <h2>Morris County</h2>
  <p>We only buy and renovate homes in our neighborhoods right here in the Morris County, NJ area. Is a house in your neighborhood an eyesore? Is it vacant, boarded up and a hazard to the neighborhood..</p>
  <a>READ MORE &gt;&gt;</a>
</div>
<div class="abs market-img" style="left:378px;top:633px;background:linear-gradient(180deg,#4a4f72,#c98a8a 40%,#3a4460 65%,#1e2438)" role="img" aria-label="Photo of a city skyline across the water at dusk"></div>
<div class="abs market-text" style="left:539px;top:630px">
  <h2>New Jersey</h2>
  <p>We only buy and renovate homes in our neighborhoods right here in the Morris County, NJ area. Is a house in your neighborhood an eyesore? Is it vacant, boarded up and a hazard to the neighborhood..</p>
  <a>READ MORE &gt;&gt;</a>
</div>

<h2 class="abs section-title portfolio-title">Our Portfolio</h2>
<svg class="abs arrow" style="left:42px" width="8" height="16" viewBox="0 0 8 16"><path d="M7 1L1 8l6 7" fill="none" stroke="#aaa" stroke-width="1.4"/></svg>
<svg class="abs arrow" style="left:676px" width="8" height="16" viewBox="0 0 8 16"><path d="M1 1l6 7-6 7" fill="none" stroke="#aaa" stroke-width="1.4"/></svg>
<div class="abs proj" style="left:60px;top:832px">
  <div class="ph" style="background:linear-gradient(180deg,#c9cbcc,#b9a88c 55%,#6f6a55)" role="img" aria-label="Photo of a renovated house in Rockaway"></div>
  <h3>Rockaway, NJ</h3><p>Many upgrades to this home, Added a new full bath, family room, office,</p>
</div>
<div class="abs proj" style="left:214px;top:832px">
  <div class="ph" style="background:linear-gradient(180deg,#5f7a3e,#d9d2bd 45%,#5d7d3a)" role="img" aria-label="Photo of a rebuilt colonial house in Denville"></div>
  <h3>Denville, NJ</h3><p>House was torn down. Using portions of the foundation and an existing</p>
</div>
<div class="abs proj" style="left:369px;top:832px">
  <div class="ph" style="background:linear-gradient(180deg,#3f5a2a,#7da0b0 50%,#5f8a3a)" role="img" aria-label="Photo of a small remodeled bungalow in Boonton"></div>
  <h3>Boonton, NJ</h3><p>A complete remodel and add on to this 2 bedroom house.</p>
</div>
<div class="abs proj" style="left:523px;top:832px">
  <div class="ph" style="background:linear-gradient(180deg,#b8c2c8,#d8d8d4 45%,#8a8272 75%,#6c8a3f)" role="img" aria-label="Photo of a house with a stone retaining wall in Rockaway"></div>
  <h3>Rockaway, NJ</h3><p>Radiant heat installed in basement and first floor bathroom, office</p>
</div>

<footer class="abs foot"></footer>
<div class="abs foot-brand"><span>Birchstone<br>Holdings</span></div>
<div class="abs vsep" style="left:336px"></div>
<div class="abs vsep" style="left:520px"></div>
<h3 class="abs foot" style="all:unset;position:absolute;left:250px;top:1036px;font-family:'Cinzel',serif;font-size:11px;color:#fff">Information</h3>
<div class="abs foot-links" style="left:250px;top:1058px">Home<br>About<br>Contact<br>Portfolio</div>
<h3 class="abs" style="left:354px;top:1036px;font-family:'Cinzel',serif;font-weight:400;font-size:11px;color:#fff">Newsletter</h3>
<div class="abs foot-small" style="left:354px;top:1062px">Register your email address to get<br>information about us</div>
<div class="abs input">Email Address</div>
<div class="abs sub-btn">SUBSCRIBE</div>
<h3 class="abs" style="left:538px;top:1036px;font-family:'Cinzel',serif;font-weight:400;font-size:11px;color:#fff">Contact Us</h3>
<div class="abs foot-row" style="top:1063px">
  <svg width="6" height="8" viewBox="0 0 6 8"><path d="M3 0a3 3 0 013 3c0 2-3 5-3 5S0 5 0 3a3 3 0 013-3z" fill="#fff"/><circle cx="3" cy="3" r="1" fill="#1c1c1c"/></svg>
  <span>Birchstone Holdings<br>Morris County, NJ</span></div>
<div class="abs foot-row" style="top:1102px">
  <svg width="8" height="8" viewBox="0 0 24 24"><path fill="#fff" d="M6.6 10.8a15 15 0 006.6 6.6l2.2-2.2a1 1 0 011-.25 11.4 11.4 0 003.6.57 1 1 0 011 1V20a1 1 0 01-1 1A17 17 0 013 4a1 1 0 011-1h3.5a1 1 0 011 1 11.4 11.4 0 00.57 3.6 1 1 0 01-.25 1z"/></svg>
  <span>+1 555-014-2290</span></div>
<div class="abs foot-row" style="top:1128px">
  <svg width="8" height="7" viewBox="0 0 24 18"><path fill="#fff" d="M0 0h24v18H0z"/><path fill="none" stroke="#1c1c1c" stroke-width="2.5" d="M1 1l11 9 11-9"/></svg>
  <span>info@@birchstoneholdings.example</span></div>
<div class="abs hsep"></div>
<div class="abs copy">Copyrights © 2016, Birchstone Holdings. All rights reserved.</div>
<div class="abs foot-social"><i></i><i></i><i></i><i></i></div>
</body>
</html>
```